Title: “The Copper Harbor, Charting The Tides of Memory, A Sailor’s Notebook”

Cover design for ebook and printable book. Looking for this specific designer

```html
<!DOCTYPE html>
<html lang="en">
<head>
<meta charset="utf-8">
<title>The Copper Harbor — Tom Avery</title>
<link rel="stylesheet" href="https://fonts.googleapis.com/css2?family=Anton&family=Oswald:wght@400;500;700&family=Parisienne&display=swap">
<style>
  :root {
    --red-core: #c0000f;
    --red-mid: #970009;
    --red-deep: #560004;
    --ink: #ffffff;
    --glow: rgba(255, 225, 225, 0.35);
  }
  html, body {
    margin: 0;
    padding: 0;
    width: 750px;
    height: 1200px;
    overflow: hidden;
    background: var(--red-deep);
  }
  .cover {
    position: relative;
    width: 750px;
    height: 1200px;
    overflow: hidden;
    background:
      radial-gradient(ellipse 70% 55% at 45% 50%, var(--red-core) 0%, var(--red-mid) 55%, var(--red-deep) 100%);
    color: var(--ink);
  }
  .author {
    position: absolute;
    top: 92px;
    left: 0;
    width: 750px;
    text-align: center;
    font-family: "Oswald", sans-serif;
    font-weight: 400;
    font-size: 58px;
    letter-spacing: 1px;
    line-height: 1;
  }
  .heart-decoration {
    position: absolute;
    top: 220px;
    left: 0;
    width: 730px;
    height: 600px;
    background:
      radial-gradient(ellipse 45% 40% at 38% 30%, var(--glow) 0%, rgba(255,255,255,0) 70%),
      radial-gradient(ellipse 40% 38% at 72% 32%, rgba(255,235,235,0.28) 0%, rgba(255,255,255,0) 70%),
      radial-gradient(ellipse 35% 45% at 55% 72%, rgba(255,220,220,0.18) 0%, rgba(255,255,255,0) 70%);
  }
  .title-block {
    position: absolute;
    top: 300px;
    left: 0;
    width: 750px;
    height: 600px;
  }
  .title-the {
    font-family: "Parisienne", cursive;
    font-size: 100px;
    fill: var(--ink);
  }
  .title-main {
    font-family: "Anton", sans-serif;
    fill: var(--ink);
  }
  .title-rule {
    stroke: var(--ink);
    stroke-width: 3;
  }
  .subtitle {
    position: absolute;
    top: 900px;
    left: 0;
    width: 750px;
    text-align: center;
    font-family: "Oswald", sans-serif;
    font-weight: 700;
    font-size: 37px;
    letter-spacing: 0.3px;
    line-height: 1;
  }
  .tagline {
    position: absolute;
    top: 970px;
    left: 0;
    width: 750px;
    text-align: center;
    font-family: "Parisienne", cursive;
    font-size: 64px;
    line-height: 1;
  }
</style>
</head>
<body>
  <main class="cover">
    <div class="author">TOM AVERY</div>

    <div class="heart-decoration" role="img" aria-label="Large heart outline formed by white halftone dots, trailing into a wave of dots on the left"></div>

    <svg class="title-block" width="750" height="600" viewBox="0 0 750 600" aria-label="The Copper Harbor">
      <text class="title-the" x="235" y="140">The</text>
      <line class="title-rule" x1="362" y1="110" x2="630" y2="110"/>
      <circle cx="362" cy="110" r="4" fill="#fff"/>
      <circle cx="630" cy="110" r="4" fill="#fff"/>
      <text class="title-main" x="375" y="250" font-size="112" text-anchor="middle" textLength="520" lengthAdjust="spacingAndGlyphs">Copper</text>
      <text class="title-main" x="378" y="565" font-size="325" text-anchor="middle" textLength="540" lengthAdjust="spacingAndGlyphs">HARBOR</text>
    </svg>

    <div class="subtitle">CHARTING THE TIDES OF MEMORY</div>
    <div class="tagline">A Sailor’s Notebook</div>
  </main>
</body>
</html>
```